Brightfern Development Corporation
Can I please see design #42 with the symbols to designate the Phone, Fax, Email and Address? Thanks.
I also like the back of the business card on design 43-45.
I like the cards that do not have too much red and over power the business card. I do like the symbols to designate phone, fax, email, address and the website information. I would like some color on the card though. I do not like the cards that are all white.
The logo should be uploaded now. Off to a good start, but please don't forget the stationary. We are looking for letterhead, envelopes, etc.

```html
<!DOCTYPE html>
<html lang="en">
<head>
<meta charset="utf-8">
<title>Brightfern Development Corporation – Stationery</title>
<link href="https://fonts.googleapis.com/css2?family=Open+Sans:wght@400;600;700&display=swap" rel="stylesheet">
<style>
:root{
  --red:#e8493a;
  --red-dark:#c93a2d;
  --ink:#333;
  --muted:#777;
  --line:#bdbdbd;
  --cell:#d9d9d9;
  --paper:#fff;
  --bg:#fff;
  --faint:#fbe6e2;
}
*{box-sizing:border-box;margin:0;padding:0}
html,body{width:1200px;height:552px;overflow:hidden;background:var(--bg);font-family:"Open Sans",Arial,sans-serif;color:var(--ink)}
.canvas{position:relative;width:1200px;height:552px}
.sheet{position:absolute;background:var(--paper);box-shadow:0 1px 4px rgba(0,0,0,.25)}
.sheet::after{content:"";position:absolute;left:0;right:0;bottom:0;height:5px;background:var(--red)}
.fax-sheet{left:24px;top:12px;width:350px;height:509px}
.letterhead{left:403px;top:12px;width:355px;height:509px}

.brand{position:absolute;display:flex;align-items:center;gap:4px;font-weight:700;color:var(--red);white-space:nowrap;line-height:1}
.brand .mark{display:block;background:currentColor}
.brand-sm{font-size:8px}
.brand-sm .mark{width:7px;height:7px}
.brand-head{left:14px;top:16px;flex-direction:column;align-items:flex-start;gap:2px;font-size:9px}
.brand-head small{font-size:4.5px;font-weight:700;color:var(--ink);letter-spacing:.3px}
.brand-foot{right:12px;bottom:14px}
.faint-name{position:absolute;left:24px;top:250px;font-size:46px;font-weight:700;color:var(--faint);line-height:1}

.contact{position:absolute;list-style:none;font-size:4.6px;line-height:6.6px;color:var(--muted)}
.contact li{display:flex;align-items:center;gap:3px}
.contact li::before{content:"";width:3px;height:3px;border-radius:50%;background:var(--red);flex:none}
.sheet .contact{left:224px;top:13px}

.fax-label{position:absolute;right:22px;top:64px;font-size:9px;color:var(--ink)}
.fax-table{position:absolute;left:14px;top:76px;width:318px;border-collapse:collapse;font-size:5px}
.fax-table td{border:1px solid var(--line);height:15px;padding:0 4px}
.fax-table td.label{background:var(--cell);width:34px}
.options{position:absolute;left:14px;top:148px;display:flex;gap:20px;font-size:4.8px;list-style:none}
.options li{display:flex;align-items:center;gap:3px}
.options li::before{content:"";width:6px;height:6px;border:1px solid #888;background:#fff}

.card{position:absolute;top:19px;height:94px;box-shadow:0 1px 4px rgba(0,0,0,.25)}
.card-front{left:778px;width:151px;background:var(--paper)}
.card-front::after{content:"";position:absolute;left:0;right:0;bottom:0;height:6px;background:var(--red)}
.card-front .brand-head{left:7px;top:8px;font-size:7px}
.card-front .band{position:absolute;left:0;top:36px;width:80px;height:14px;background:var(--red)}
.card-front .contact{left:7px;top:54px;font-size:4px;line-height:5.6px}
.card-holder{position:absolute;right:8px;top:9px;text-align:left;font-size:5.5px;font-weight:700;color:var(--red)}
.card-holder span{display:block;font-size:4px;font-weight:400;color:var(--muted)}
.card-back{left:943px;width:185px;background:var(--red);border-radius:3px}
.card-back .brand{left:50%;top:50%;transform:translate(-50%,-50%);color:#fff;font-size:11px}
.card-back .brand .mark{width:9px;height:9px}

.envelope{position:absolute;left:775px;width:406px;box-shadow:0 1px 4px rgba(0,0,0,.25);background:var(--paper)}
.envelope-front{top:120px;height:216px}
.envelope-front .brand-head{left:12px;top:14px;font-size:10px}
.envelope-front .contact{left:110px;top:40px}
.envelope-front .band{position:absolute;left:0;right:0;bottom:58px;height:4px;background:var(--red)}
.envelope-front .brand-foot{right:20px;bottom:70px;font-size:11px}
.envelope-front .brand-foot .mark{width:9px;height:9px}
.envelope-back{top:341px;height:177px;overflow:hidden}
.envelope-back svg{position:absolute;left:0;top:0}
.envelope-back .brand{left:50%;top:34px;transform:translateX(-50%);color:#fff;font-size:10px}
.envelope-back .brand .mark{width:8px;height:8px}
</style>
</head>
<body>
<main class="canvas">

  <article class="sheet fax-sheet">
    <div class="brand brand-head">Brightfern<small>DEVELOPMENT CORPORATION</small></div>
    <ul class="contact">
      <li>1840 Larkspur Avenue, Suite 200</li>
      <li>Phone: 555-014-2288</li>
      <li>Fax: 555-014-2289</li>
      <li>info@brightfern.example</li>
      <li>www.brightfern.example</li>
    </ul>
    <div class="fax-label">FAX</div>
    <table class="fax-table">
      <tr><td class="label">To:</td><td></td><td class="label">From:</td><td></td></tr>
      <tr><td class="label">Fax:</td><td></td><td class="label">Pages:</td><td></td></tr>
      <tr><td class="label">Phone:</td><td></td><td class="label">Date:</td><td></td></tr>
      <tr><td class="label">Re:</td><td></td><td class="label">CC:</td><td></td></tr>
    </table>
    <ul class="options">
      <li>Urgent</li><li>For Review</li><li>Please Comment</li><li>Please Reply</li><li>Please Recycle</li>
    </ul>
    <div class="faint-name" aria-hidden="true">Brightfern</div>
    <div class="brand brand-sm brand-foot"><span class="mark"></span>Brightfern</div>
  </article>

  <article class="sheet letterhead">
    <div class="brand brand-head">Brightfern<small>DEVELOPMENT CORPORATION</small></div>
    <ul class="contact">
      <li>1840 Larkspur Avenue, Suite 200</li>
      <li>Phone: 555-014-2288</li>
      <li>Fax: 555-014-2289</li>
      <li>info@brightfern.example</li>
      <li>www.brightfern.example</li>
    </ul>
    <div class="faint-name" aria-hidden="true">Brightfern</div>
    <div class="brand brand-sm brand-foot"><span class="mark"></span>Brightfern</div>
  </article>

  <article class="card card-front">
    <div class="brand brand-head">Brightfern<small>DEVELOPMENT CORPORATION</small></div>
    <div class="card-holder">Dana Reyes<span>Project Director</span></div>
    <div class="band"></div>
    <ul class="contact">
      <li>1840 Larkspur Avenue, Suite 200</li>
      <li>Phone: 555-014-2288</li>
      <li>Fax: 555-014-2289</li>
      <li>info@brightfern.example</li>
    </ul>
  </article>

  <article class="card card-back">
    <div class="brand"><span class="mark"></span>Brightfern</div>
  </article>

  <article class="envelope envelope-front">
    <div class="brand brand-head">Brightfern<small>DEVELOPMENT CORPORATION</small></div>
    <ul class="contact">
      <li>1840 Larkspur Avenue, Suite 200</li>
      <li>Phone: 555-014-2288</li>
      <li>Fax: 555-014-2289</li>
      <li>info@brightfern.example</li>
    </ul>
    <div class="brand brand-foot"><span class="mark"></span>Brightfern</div>
    <div class="band"></div>
  </article>

  <article class="envelope envelope-back">
    <svg width="406" height="177" viewBox="0 0 406 177" aria-hidden="true">
      <path d="M0 0H406V58L214 92Q203 94 192 92L0 58Z" fill="var(--red)"/>
    </svg>
    <div class="brand"><span class="mark"></span>Brightfern</div>
  </article>

</main>
</body>
</html>
```